I need email signatures for my admin staff members
info:
Darina Qubrosi
Support Coordinator
Unit 4, 517 Wattlebrook Lane, Kemberly NSW 2893
Tel: 02 84427193 Mob: 0427596314
email: darina.qu@mivrotelhaven.com
www.mivrotelhaven.com

Target Market(s)

community services industry

Industry/Entity Type

Community Service

Requirements
Must have
• Specialist Provider of Multicultural Support Services
Nice to have
• "I acknowledge the traditional owners of the land on which we live, work and dream"
plus their flags as attached

```html
<!DOCTYPE html>
<html lang="en">
<head>
<meta charset="utf-8">
<title>Email Signature – Darina Qubrosi</title>
<link href="https://fonts.googleapis.com/css2?family=Lato:ital,wght@0,400;0,700;1,400&display=swap" rel="stylesheet">
<style>
  :root {
    --orange: #f7931e;
    --charcoal: #333333;
    --ink: #222222;
    --paper: #ffffff;
    --backdrop: #dcdcdc;
    --flag-dark: #5a2a2a;
    --flag-cool: #2c3f8f;
  }
  html, body {
    margin: 0;
    padding: 0;
    width: 1200px;
    height: 794px;
    overflow: hidden;
    background: var(--backdrop);
    font-family: "Lato", sans-serif;
  }
  .signature {
    position: absolute;
    left: 0;
    top: 171px;
    width: 1200px;
    height: 451px;
    background: var(--paper);
  }
  .side-band-top {
    position: absolute; left: 0; top: 0;
    width: 63px; height: 174px;
    background: var(--orange);
  }
  .side-band-bottom {
    position: absolute; left: 0; top: 179px;
    width: 63px; height: 272px;
    background: var(--charcoal);
  }
  .person {
    position: absolute; left: 80px; top: 50px;
  }
  .person-name {
    margin: 0;
    font-size: 38px; font-weight: 700;
    color: var(--orange);
    line-height: 1;
  }
  .person-role {
    margin: 4px 0 0 2px;
    font-size: 29px;
    color: var(--ink);
    line-height: 1;
  }
  .acknowledgement {
    position: absolute; left: 521px; top: 52px;
    margin: 0;
    font-size: 24px;
    line-height: 31px;
    color: var(--ink);
    width: 478px;
  }
  .flags-placeholder {
    position: absolute; left: 1008px; top: 71px;
    width: 140px; height: 48px;
    background: linear-gradient(90deg, var(--flag-dark), var(--flag-cool));
  }
  .contact-icon {
    position: absolute; left: 9px;
    width: 36px; height: 36px;
  }
  .contact-line {
    position: absolute; left: 77px;
    margin: 0;
    font-size: 29px;
    line-height: 1;
    color: var(--ink);
    transform: translateY(-50%);
    white-space: nowrap;
  }
  .contact-line.address { left: 79px; font-size: 30px; }
  .brand {
    position: absolute; left: 780px; top: 166px;
    width: 404px;
    text-align: center;
  }
  .brand-mark {
    display: block;
    margin: 0 auto;
    width: 112px; height: 112px;
    border-radius: 50%;
    background: var(--orange);
  }
  .brand-name {
    margin: 12px 0 0;
    font-size: 30px; font-weight: 700;
    letter-spacing: 2px;
    color: var(--orange);
    line-height: 1;
  }
  .brand-tagline {
    margin: 16px 0 0;
    font-size: 25px; font-style: italic;
    color: var(--orange);
    line-height: 29px;
  }
</style>
</head>
<body>
  <section class="signature">
    <div class="side-band-top"></div>
    <div class="side-band-bottom"></div>

    <div class="person">
      <h1 class="person-name">Darina Qubrosi</h1>
      <p class="person-role">Support Coordinator</p>
    </div>

    <p class="acknowledgement">“I acknowledge the traditional owners of the land on&nbsp; which we live, work and dream”</p>

    <div class="flags-placeholder" role="img" aria-label="Flags of the traditional owners of the land"></div>

    <svg class="contact-icon" style="top:210px" viewBox="0 0 36 36" aria-hidden="true">
      <circle cx="18" cy="18" r="18" fill="var(--orange)"/>
      <path d="M12 9c1.2-.8 2.3-.5 2.9.6l1.6 3c.5 1 .2 1.9-.7 2.5l-1 .6c.8 2.2 2.3 3.9 4.4 5l.7-1c.6-.8 1.6-1 2.5-.5l2.9 1.7c1 .6 1.2 1.7.4 2.8-1.6 2.1-4 2.5-6.7 1-4-2.2-6.9-5.6-8-9.8-.6-2.4.1-4.6 1-5.900z" fill="var(--charcoal)"/>
    </svg>
    <p class="contact-line" style="top:228px">02 84427193</p>

    <svg class="contact-icon" style="top:251px" viewBox="0 0 36 36" aria-hidden="true">
      <circle cx="18" cy="18" r="18" fill="var(--orange)"/>
      <rect x="11" y="8" width="14" height="20" rx="2" fill="none" stroke="var(--charcoal)" stroke-width="2.5"/>
      <line x1="11" y1="23.5" x2="25" y2="23.5" stroke="var(--charcoal)" stroke-width="2"/>
    </svg>
    <p class="contact-line" style="top:269px">0427596314</p>

    <svg class="contact-icon" style="top:291px" viewBox="0 0 36 36" aria-hidden="true">
      <circle cx="18" cy="18" r="18" fill="var(--orange)"/>
      <rect x="8" y="11" width="20" height="14" fill="none" stroke="var(--charcoal)" stroke-width="2.2"/>
      <path d="M8 11l10 8 10-8M8 25l7-7M28 25l-7-7" fill="none" stroke="var(--charcoal)" stroke-width="1.8"/>
    </svg>
    <p class="contact-line" style="top:309px">darina.qu@mivrotelhaven.com</p>

    <svg class="contact-icon" style="top:332px" viewBox="0 0 36 36" aria-hidden="true">
      <circle cx="18" cy="18" r="18" fill="var(--orange)"/>
      <circle cx="18" cy="18" r="10" fill="none" stroke="var(--charcoal)" stroke-width="2.5"/>
      <path d="M12 12c3 1 4 3 3 5s1 3 3 3 2 3 1 6M22 9c0 3 2 4 5 4" fill="none" stroke="var(--charcoal)" stroke-width="2.2"/>
    </svg>
    <p class="contact-line" style="top:350px">www.mivrotelhaven.com</p>

    <svg class="contact-icon" style="top:382px" viewBox="0 0 36 36" aria-hidden="true">
      <circle cx="18" cy="18" r="18" fill="var(--orange)"/>
      <path d="M18 29c-5-6-8-10-8-14a8 8 0 0 1 16 0c0 4-3 8-8 14z" fill="var(--charcoal)"/>
      <circle cx="18" cy="15" r="3.2" fill="var(--orange)"/>
    </svg>
    <p class="contact-line address" style="top:400px">Unit 4, 517 Wattlebrook Lane, Kemberly NSW 2893</p>

    <div class="brand">
      <span class="brand-mark"></span>
      <p class="brand-name">MIVROTEL HAVEN</p>
      <p class="brand-tagline">Specialist Provider of&nbsp; Multicultural<br>Support Services</p>
    </div>
  </section>
</body>
</html>
```